KORVELTA Corporate Business Card

Modern business card design for company which focuses in the areas of Staffing, IT Consulting & Data Services. Please note: We are no longer using the IT subscript on the logo. All designs should have IT subscript removed.
Website: www.korveltait.example

```html
<!DOCTYPE html>
<html lang="en">
<head>
<meta charset="utf-8">
<title>KORVELTA Business Card</title>
<link href="https://fonts.googleapis.com/css2?family=Exo+2:wght@600;700&family=Lato:wght@400&display=swap" rel="stylesheet">
<style>
  :root {
    --page-bg: #e4ded6;
    --card-white: #ffffff;
    --card-blue: #075a94;
    --brand-blue: #1f9ad6;
    --icon-blue: #0b5c96;
    --text-grey: #4a4a4a;
    --text-white: #ffffff;
  }
  html, body {
    margin: 0;
    padding: 0;
    width: 900px;
    height: 1200px;
    overflow: hidden;
    background: var(--page-bg);
  }
  .canvas {
    position: relative;
    width: 900px;
    height: 1200px;
  }
  .card {
    position: absolute;
    left: 86px;
    width: 736px;
    height: 430px;
    border-radius: 24px;
    box-shadow: 0 6px 14px rgba(0,0,0,0.25);
    overflow: hidden;
  }
  .card--front { top: 137px; background: var(--card-white); }
  .card--back { top: 633px; background: var(--card-blue); }

  .brand-name {
    position: absolute;
    margin: 0;
    font-family: "Exo 2", sans-serif;
    font-weight: 700;
    color: var(--brand-blue);
    letter-spacing: 2px;
    line-height: 1;
    white-space: nowrap;
  }
  .card--front .brand-name {
    right: 52px;
    top: 58px;
    font-size: 66px;
  }
  .card--back .brand-name {
    left: 0;
    right: 0;
    top: 172px;
    text-align: center;
    font-size: 92px;
  }

  .person {
    position: absolute;
    left: 53px;
    top: 213px;
  }
  .person__name {
    margin: 0;
    font-family: "Exo 2", sans-serif;
    font-weight: 700;
    font-size: 28px;
    letter-spacing: 1px;
    color: var(--brand-blue);
    line-height: 1.1;
  }
  .person__role {
    margin: 4px 0 0;
    font-family: "Lato", sans-serif;
    font-size: 17px;
    color: var(--text-grey);
  }

  .contact-list {
    position: absolute;
    left: 53px;
    top: 293px;
    margin: 0;
    padding: 0;
    list-style: none;
    font-family: "Lato", sans-serif;
    font-size: 17px;
    color: var(--text-grey);
  }
  .contact-list li {
    display: flex;
    align-items: center;
    height: 29px;
  }
  .contact-list svg {
    width: 13px;
    height: 13px;
    margin-right: 10px;
    fill: var(--icon-blue);
  }

  .address {
    position: absolute;
    right: 52px;
    top: 322px;
    margin: 0;
    font-family: "Lato", sans-serif;
    font-style: normal;
    font-size: 17px;
    line-height: 29px;
    color: var(--text-grey);
    text-align: right;
  }

  .website {
    position: absolute;
    left: 0;
    right: 0;
    top: 369px;
    margin: 0;
    text-align: center;
    font-family: "Lato", sans-serif;
    font-size: 19px;
    letter-spacing: 0.5px;
    color: var(--text-white);
  }
  .website__domain { color: var(--brand-blue); }
</style>
</head>
<body>
<main class="canvas">
  <section class="card card--front">
    <h1 class="brand-name">KORVELTA</h1>

    <div class="person">
      <h2 class="person__name">DALIA RENNER</h2>
      <p class="person__role">Founder &amp; CEO</p>
    </div>

    <ul class="contact-list">
      <li>
        <svg viewBox="0 0 16 16" aria-hidden="true"><path d="M3.6 1.2l2.3 2.6-1.3 1.9c.9 2 2.5 3.6 4.5 4.6l1.9-1.3 2.6 2.3-1.3 2.6C7 13.8 2.2 9 1 3.1z"/></svg>
        555-014-2760
      </li>
      <li>
        <svg viewBox="0 0 16 16" aria-hidden="true"><path d="M1 3h14v1.5L8 9 1 4.5z"/><path d="M1 6.2L8 10.6l7-4.4V13H1z"/></svg>
        contactus@korveltait.example
      </li>
      <li>
        <svg viewBox="0 0 16 16" aria-hidden="true"><path d="M8 1a7 7 0 100 14A7 7 0 008 1zm0 1.6c.7.8 1.3 2.1 1.5 3.6h-3c.2-1.5.8-2.8 1.5-3.6zM2.7 7.2h2.5c0 .3 0 .5 0 .8s0 .6.1.8H2.7a5.4 5.4 0 010-1.6zm3.8 0h3c0 .3.1.5.1.8s0 .6-.1.8h-3c0-.3-.1-.5-.1-.8s0-.5.1-.8zm4.3 0h2.5a5.4 5.4 0 010 1.6h-2.5c0-.3.1-.5.1-.8s0-.5-.1-.8zM6.5 9.8h3c-.2 1.5-.8 2.8-1.5 3.6-.7-.8-1.3-2.1-1.5-3.6z"/></svg>
        http://www.korveltait.example
      </li>
    </ul>

    <address class="address">410 Harbor Ln.<br>Millbrook, OH 45021</address>
  </section>

  <section class="card card--back">
    <h1 class="brand-name">KORVELTA</h1>
    <p class="website">www.<span class="website__domain">korveltait</span>.example</p>
  </section>
</main>
</body>
</html>
```